Covid19 Poster for workplaces

Create a poster on how to protect yourself from Corona virus at work.
We are a Staff Harbour company. We have just re-branded so we need to fit in with our brand. We like clean and fresh, slightly amusing is ok if it will draw attention but it's an important topic. A4 and A3 please.

Content:

Headline: Lower the risk of COVID 19 in the workplace.

BE WELL

Bring your own cup - don’t share cups and food.
Elbow tap instead of handshakes and kisses
Wash your hands often - with soap.
Elbow or tissues when you cough or sneeze then straight in the bin
Leave your face alone after touching shared surfaces
Leave your bugs at home if you’re feeling unwell.

Call health line if you have a cough, a high temperature and shortness of breath. 0800 472 9160

Based on recommendations from IPB and DCT

Target Market(s)

Employees - so anyone

Other font styles liked:
• Use the closest font to the brand documents

Requirements
Should not have
• Clip art

```html
<!DOCTYPE html>
<html lang="en">
<head>
<meta charset="utf-8">
<title>Lower the risk of COVID 19 in the workplace</title>
<link rel="stylesheet" href="https://fonts.googleapis.com/css2?family=Work+Sans:wght@500;600;700;800&display=swap">
<style>
  :root {
    --teal: #1fb0b8;
    --teal-dark: #138a91;
    --yellow: #f6ea16;
    --white: #ffffff;
    --ink: #111111;
    --icon-fill: #e9f7f8;
  }
  * { margin: 0; padding: 0; box-sizing: border-box; }
  html, body { width: 849px; height: 1200px; overflow: hidden; }
  body { background: var(--teal); font-family: "Work Sans", Arial, sans-serif; color: var(--white); }
  .poster { position: relative; width: 849px; height: 1200px; background: var(--teal); overflow: hidden; }

  .headline { position: absolute; top: 40px; left: 0; width: 100%; text-align: center; font-weight: 800; line-height: 1; }
  .headline .lead { display: block; font-size: 56px; letter-spacing: -0.5px; }
  .headline .virus { display: block; color: var(--yellow); font-size: 112px; margin-top: 8px; letter-spacing: -1px; }
  .headline .place { display: block; font-size: 56px; margin-top: 6px; letter-spacing: -0.5px; }

  .divider { position: absolute; left: 423px; top: 311px; width: 3px; height: 454px; background: var(--white); }

  .tip { position: absolute; display: flex; align-items: center; }
  .tip-icon { width: 106px; height: 106px; border-radius: 50%; background: var(--icon-fill); border: 4px solid var(--yellow); flex: none; }
  .tip-text { margin-left: 18px; font-size: 15.5px; line-height: 1.32; font-weight: 500; }
  .tip-label { display: inline-block; background: var(--yellow); color: var(--teal-dark); font-weight: 700; font-size: 18px; padding: 1px 4px; margin-bottom: 4px; }

  .tip-cup { left: 64px; top: 326px; }
  .tip-tap { left: 64px; top: 470px; }
  .tip-wash { left: 64px; top: 613px; }
  .tip-cough { left: 460px; top: 328px; }
  .tip-face { left: 460px; top: 470px; }
  .tip-home { left: 460px; top: 604px; }

  .helpline { position: absolute; left: 204px; top: 792px; }
  .helpline-icon { position: absolute; left: 0; top: 22px; width: 102px; height: 104px; border-radius: 50% 50% 46% 46%; background: var(--yellow); }
  .helpline-body { position: absolute; left: 128px; top: 0; width: 400px; }
  .helpline-note { font-size: 15.5px; line-height: 1.3; font-weight: 500; }
  .helpline-label { display: inline-block; margin-top: 8px; background: var(--yellow); color: var(--teal-dark); font-weight: 700; font-size: 18px; padding: 1px 4px; }
  .helpline-number { font-size: 45px; font-weight: 700; letter-spacing: 0.5px; margin-top: 2px; white-space: nowrap; line-height: 1.1; }

  .sources { position: absolute; left: 113px; top: 940px; width: 640px; height: 60px; }
  .sources-note { position: absolute; left: 0; top: 14px; color: var(--yellow); font-weight: 700; font-size: 15px; line-height: 1.3; }
  .source-name { position: absolute; top: 8px; font-weight: 700; font-size: 34px; color: var(--white); }
  .source-ipb { left: 226px; }
  .source-dct { left: 464px; }

  .brand-panel { position: absolute; left: 142px; top: 1054px; width: 566px; height: 160px; background: var(--white); border-radius: 44px 44px 0 0; }
  .brand-dot { position: absolute; left: 86px; top: 34px; width: 84px; height: 84px; border-radius: 50%; background: var(--teal); }
  .brand-name { position: absolute; left: 232px; top: 20px; font-weight: 800; font-size: 54px; line-height: 0.98; color: var(--ink); letter-spacing: -1px; }
</style>
</head>
<body>
<main class="poster">
  <h1 class="headline">
    <span class="lead">Lower the risk of</span>
    <span class="virus">COVID 19</span>
    <span class="place">in the workplace.</span>
  </h1>

  <div class="divider"></div>

  <section class="tip tip-cup">
    <div class="tip-icon" role="img" aria-label="Illustration of a hand holding a reusable cup"></div>
    <p class="tip-text"><span class="tip-label">Bring your own cup</span><br>don't share cups and food.</p>
  </section>
  <section class="tip tip-tap">
    <div class="tip-icon" role="img" aria-label="Illustration of two elbows tapping"></div>
    <p class="tip-text"><span class="tip-label">Elbow Tap</span><br>instead of handshakes<br>and kisses</p>
  </section>
  <section class="tip tip-wash">
    <div class="tip-icon" role="img" aria-label="Illustration of hands washing under a tap"></div>
    <p class="tip-text"><span class="tip-label">Washing Hand</span><br>Wash your hands often<br>with soap</p>
  </section>

  <section class="tip tip-cough">
    <div class="tip-icon" role="img" aria-label="Illustration of a person coughing into an elbow"></div>
    <p class="tip-text"><span class="tip-label">Use Elbow or tissues</span><br>when you cough or sneez<br>then straight in the bin</p>
  </section>
  <section class="tip tip-face">
    <div class="tip-icon" role="img" aria-label="Illustration of a person wearing a face mask"></div>
    <p class="tip-text"><span class="tip-label">Use Masker</span><br>Leave your face alone after<br>touching shared surfaces</p>
  </section>
  <section class="tip tip-home">
    <div class="tip-icon" role="img" aria-label="Illustration of an unwell person staying at home"></div>
    <p class="tip-text">Leave your bugs at home<br>if you're feeling unwell.</p>
  </section>

  <section class="helpline">
    <div class="helpline-icon" role="img" aria-label="Illustration of a health line support headset"></div>
    <div class="helpline-body">
      <p class="helpline-note">if you have a cough,a high<br>temperature and shortness of breath.</p>
      <span class="helpline-label">Call Health Line</span>
      <p class="helpline-number">0800 472 9160</p>
    </div>
  </section>

  <section class="sources">
    <p class="sources-note">Based on<br>recommendations from</p>
    <span class="source-name source-ipb">IPB</span>
    <span class="source-name source-dct">DCT</span>
  </section>

  <footer class="brand-panel">
    <div class="brand-dot"></div>
    <p class="brand-name">Staff<br>Harbour</p>
  </footer>
</main>
</body>
</html>
```